KeyHarbor needs a modern business card

We are a modern conveyancing company and we need to appeal to the top (Multi-million dollar properties)and bottom on the property conveyancing market but our sweet spot is the middle of the market. I like professional with a hint of unconventional.

Target Market(s)

As above

Industry/Entity Type

Real Estate

Contact Information for Business Card

Back Of card:
thinking black with the logo and a tag line (I could be wrong about the black)
Tag line - Clear Advice, Smooth Handovers

Front of Card:
Marissa Toll (BBus (Finance) LLB)
Licensed Conveyancer
Email: marissa@keyharbor.com.au

Key Harbor
ABN: 48 913 706
Suite 14, Level 3, 9 Calloway Road Lindhurst Park, NSW 2178
Phone: 1300 682 917

Sydney - Melbourne - Brisbane (Perhaps have this along the bottom of the card)

Requirements
Must have
• Sleek, modern and top end appeal (But approachable)
Should not have
• Not too cluttered

```html
<!DOCTYPE html>
<html lang="en">
<head>
<meta charset="utf-8">
<title>KeyHarbor Business Card</title>
<link href="https://fonts.googleapis.com/css2?family=Arimo:wght@400;700&display=swap" rel="stylesheet">
<style>
  :root {
    --stage: #e7e4df;
    --card-black: #0b0b0b;
    --lime: #a6cf3c;
    --sky: #7fd3ee;
    --white: #ffffff;
    --brand-blue: #2a9fe0;
    --tagline-blue: #1f8fe8;
    --wordmark-grey: #8c8c8c;
    --rule: #2b3f58;
    --icon-blue: #5cc3ea;
  }
  * { margin: 0; padding: 0; box-sizing: border-box; }
  html, body { width: 1200px; height: 892px; overflow: hidden; }
  body {
    background: var(--stage);
    font-family: "Arimo", Arial, sans-serif;
    position: relative;
  }
  .card {
    position: absolute;
    left: 300px;
    width: 600px;
    height: 343px;
    background: var(--card-black);
    border-radius: 4px;
    overflow: hidden;
    box-shadow: 0 10px 28px rgba(0,0,0,.28);
  }
  .card--front { top: 78px; }
  .card--back { top: 471px; }

  /* Front */
  .front-brand {
    position: absolute;
    left: 62px;
    top: 48px;
    display: flex;
    flex-direction: column;
    align-items: center;
    gap: 16px;
  }
  .brand-square {
    width: 64px;
    height: 64px;
    background: var(--brand-blue);
  }
  .brand-name {
    color: var(--wordmark-grey);
    font-weight: 700;
    font-size: 34px;
    letter-spacing: -0.5px;
  }
  .divider {
    position: absolute;
    left: 292px;
    top: 36px;
    width: 1px;
    height: 180px;
    background: var(--rule);
  }
  .contact {
    position: absolute;
    left: 310px;
    top: 48px;
    color: var(--white);
    font-size: 15px;
    line-height: 1.5;
  }
  .contact__name {
    color: var(--lime);
    font-size: 16px;
    margin-bottom: 2px;
  }
  .contact__title { margin-bottom: 8px; }
  .contact__row {
    display: flex;
    align-items: center;
    gap: 8px;
    margin-bottom: 3px;
  }
  .contact__icon {
    width: 18px;
    height: 16px;
    flex: none;
  }
  .contact__abn { margin-top: 2px; }
  .front-band {
    position: absolute;
    left: 0;
    top: 0;
    width: 600px;
    height: 343px;
  }
  .address {
    font-family: "Arimo", Arial, sans-serif;
    font-size: 14px;
    fill: var(--card-black);
  }

  /* Back */
  .back-brand {
    position: absolute;
    left: 0;
    top: 52px;
    width: 100%;
    display: flex;
    flex-direction: column;
    align-items: center;
  }
  .back-brand .brand-square {
    width: 92px;
    height: 92px;
    margin-bottom: 18px;
  }
  .back-brand .brand-name { font-size: 62px; letter-spacing: -1px; line-height: 1; }
  .tagline {
    margin-top: 18px;
    color: var(--tagline-blue);
    font-size: 30px;
    letter-spacing: 0.2px;
  }
</style>
</head>
<body>

<section class="card card--front" aria-label="Business card front">
  <svg class="front-band" viewBox="0 0 600 343">
    <path d="M0,232 Q300,262 600,300 L600,343 L0,343 Z" fill="var(--sky)"/>
    <path d="M0,242 Q300,272 600,310 L600,343 L0,343 Z" fill="var(--white)"/>
    <path d="M0,250 Q300,282 600,320 L600,343 L0,343 Z" fill="var(--lime)"/>
    <g transform="translate(30,266) rotate(6.5)">
      <rect x="0" y="0" width="14" height="14" fill="var(--card-black)"/>
      <path d="M7,2.5 a3.5,3.5 0 0 1 3.5,3.5 c0,2.5 -3.5,6 -3.5,6 c0,0 -3.5,-3.5 -3.5,-6 a3.5,3.5 0 0 1 3.5,-3.5 z" fill="var(--white)"/>
      <circle cx="7" cy="6" r="1.3" fill="var(--card-black)"/>
      <text class="address" x="22" y="12">Suite 14, Level 3, 9 Calloway Road Lindhurst Park, NSW 2178</text>
    </g>
  </svg>

  <div class="front-brand">
    <div class="brand-square"></div>
    <div class="brand-name">KeyHarbor</div>
  </div>

  <div class="divider"></div>

  <div class="contact">
    <div class="contact__name">Marissa Toll (BBus (Finance) LLB)</div>
    <div class="contact__title">Licensed Conveyancer</div>
    <div class="contact__row">
      <svg class="contact__icon" viewBox="0 0 18 16" aria-hidden="true">
        <rect width="18" height="16" rx="1" fill="var(--icon-blue)"/>
        <path d="M5,4 l2,0 l1,2.5 l-1.3,1 a6,6 0 0 0 3,3 l1,-1.3 l2.5,1 l0,2 a1,1 0 0 1 -1,1 a9,9 0 0 1 -8.2,-8.2 a1,1 0 0 1 1,-1 z" fill="var(--card-black)"/>
      </svg>
      <span>1300 682 917</span>
    </div>
    <div class="contact__row">
      <svg class="contact__icon" viewBox="0 0 18 16" aria-hidden="true">
        <rect width="18" height="16" rx="1" fill="var(--icon-blue)"/>
        <rect x="3.5" y="4" width="11" height="8" fill="none" stroke="var(--card-black)" stroke-width="1.4"/>
        <path d="M3.5,4 L9,8.5 L14.5,4" fill="none" stroke="var(--card-black)" stroke-width="1.4"/>
      </svg>
      <span>marissa@keyharbor.com.au</span>
    </div>
    <div class="contact__abn">ABN: 48 913 706</div>
  </div>
</section>

<section class="card card--back" aria-label="Business card back">
  <div class="back-brand">
    <div class="brand-square"></div>
    <div class="brand-name">KeyHarbor</div>
    <div class="tagline">Clear Advice, Smooth Handovers</div>
  </div>
</section>

</body>
</html>
```